Q-Rolls Business Card

We are a modern retail clothing store. Established in 1994. I need a presentable card that will amaze vendors when given to them.

Front: Logo in middle
Info Side:

Name: Tomas Velder
Cell: 630-812-4463
Work: 630-917-3384 EXT. 417
Email: Tomas@q-rolls-example.com
Website: www.Q-rolls-example.com

Industry/Entity Type

Business

```html
<!DOCTYPE html>
<html lang="en">
<head>
<meta charset="utf-8">
<title>Q-Rolls Business Card</title>
<link rel="stylesheet" href="https://fonts.googleapis.com/css2?family=Saira:wght@700&family=Roboto:wght@400&display=swap">
<style>
  :root {
    --bg-top: #e4e4e4;
    --bg-bottom: #a9a9a9;
    --card-dark: #0f0f0f;
    --card-dark-edge: #262626;
    --card-light: #ffffff;
    --ink: #111111;
    --ink-soft: #555555;
    --paper-white: #ffffff;
  }
  * { box-sizing: border-box; margin: 0; padding: 0; }
  html, body { width: 1200px; height: 960px; overflow: hidden; }
  body {
    background: radial-gradient(ellipse at 55% 35%, var(--bg-top) 0%, var(--bg-bottom) 100%);
    font-family: "Roboto", Arial, sans-serif;
    position: relative;
  }
  .card {
    position: absolute;
    left: 330px;
    width: 540px;
    height: 308px;
    border-radius: 4px;
    box-shadow: 0 14px 30px rgba(0,0,0,0.28);
    overflow: hidden;
  }
  .card-front {
    top: 130px;
    background: linear-gradient(160deg, var(--card-dark-edge) 0%, var(--card-dark) 55%);
  }
  .card-back {
    top: 500px;
    background: var(--card-light);
  }
  .brand-name {
    font-family: "Roboto", Arial, sans-serif;
    font-weight: 400;
    line-height: 1;
    white-space: nowrap;
  }
  .front-name {
    position: absolute;
    inset: 0;
    display: flex;
    align-items: center;
    justify-content: center;
    color: var(--paper-white);
    font-size: 72px;
  }
  .back-name {
    position: absolute;
    left: 34px;
    top: 120px;
    color: var(--ink);
    font-size: 36px;
  }
  .holder-name {
    position: absolute;
    left: 300px;
    top: 64px;
    font-family: "Saira", Arial, sans-serif;
    font-weight: 700;
    font-size: 26px;
    line-height: 1.2;
    color: var(--ink);
    white-space: nowrap;
  }
  .contact-list {
    position: absolute;
    left: 258px;
    top: 160px;
    list-style: none;
  }
  .contact-list li {
    display: flex;
    align-items: center;
    gap: 8px;
    font-size: 15px;
    line-height: 24px;
    color: var(--ink);
    white-space: nowrap;
  }
  .contact-list svg {
    width: 12px;
    height: 12px;
    flex: none;
  }
  .icon-stroke { fill: none; stroke: var(--ink-soft); stroke-width: 1.4; }
  .icon-fill { fill: var(--ink-soft); }
</style>
</head>
<body>
  <section class="card card-front" aria-label="Card front">
    <span class="brand-name front-name">Q-Rolls</span>
  </section>

  <section class="card card-back" aria-label="Card back">
    <span class="brand-name back-name">Q-Rolls</span>
    <h1 class="holder-name">Tomas Velder</h1>
    <ul class="contact-list">
      <li>
        <svg viewBox="0 0 12 12" aria-hidden="true"><rect class="icon-stroke" x="3" y="0.8" width="6" height="10.4" rx="1"/><circle class="icon-fill" cx="6" cy="9.4" r="0.7"/></svg>
        630-812-4463
      </li>
      <li>
        <svg viewBox="0 0 12 12" aria-hidden="true"><path class="icon-fill" d="M3 1 L5 3.4 L4 4.6 C4.6 6 5.8 7.3 7.4 8 L8.6 7 L11 9 L9.6 11 C5.4 10.6 1.4 6.6 1 2.4 Z"/></svg>
        630-917-3384 Ext. 417
      </li>
      <li>
        <svg viewBox="0 0 12 12" aria-hidden="true"><rect class="icon-stroke" x="0.8" y="2.4" width="10.4" height="7.4"/><path class="icon-stroke" d="M0.8 2.4 L6 6.6 L11.2 2.4"/></svg>
        Tomas@q-rolls-example.com
      </li>
      <li>
        <svg viewBox="0 0 12 12" aria-hidden="true"><circle class="icon-stroke" cx="6" cy="6" r="5"/><ellipse class="icon-stroke" cx="6" cy="6" rx="2.2" ry="5"/><path class="icon-stroke" d="M1 6 H11"/></svg>
        www.Q-rolls-example.com
      </li>
    </ul>
  </section>
</body>
</html>
```